VELMOTIK Amazing Business Cards Challenge

Velmoti is a new technology company that will provide engineering and manufacturing services in the electric vehicle industry.

We are looking at a new business card that will support our orientation in providing advanced, innovative solutions. The business card will be lean and present the only information required to be more efficient.

Target Market(s)

Fleet operators, private commercial vehicle operators, delivery companies.

Industry/Entity Type

Business

Contact Information for Business Card

Use the logo and its colors, use a white background.

Font styles to use
Sans Serif

Colors
0455a3
ffffff
9bcb3c

Requirements
Must have
• Velmotik Logo
• All informations in the DOC file = 3 different cards.
• White background
Nice to have
• Icons for email, phone and web address.
• Cute design and strong identity.
Should not have
• Bleeds

```html
<!DOCTYPE html>
<html lang="en">
<head>
<meta charset="utf-8">
<title>Velmotik Business Cards</title>
<link href="https://fonts.googleapis.com/css2?family=Open+Sans:wght@400;600&display=swap" rel="stylesheet">
<style>
  :root {
    --stage: #e9eaec;
    --card: #ffffff;
    --brand-blue: #1b75bc;
    --brand-grey: #58595b;
    --text-grey: #4d4d4f;
    --rule: #3a3a3c;
  }
  * { box-sizing: border-box; margin: 0; padding: 0; }
  html, body {
    width: 1200px; height: 900px; overflow: hidden;
    background: var(--stage);
    font-family: "Open Sans", sans-serif;
  }
  .stage { position: relative; width: 1200px; height: 900px; }
  .card {
    position: absolute; width: 560px; height: 320px;
    background: var(--card);
    box-shadow: 0 6px 18px rgba(0,0,0,.12);
    overflow: hidden;
  }
  .card--front { left: 70px; top: 90px; }
  .card--back { left: 570px; top: 490px; }

  .wordmark { display: flex; align-items: center; gap: 12px; color: var(--brand-grey); font-weight: 400; letter-spacing: 1px; line-height: 1; white-space: nowrap; }
  .wordmark__square { width: 34px; height: 34px; background: var(--brand-blue); flex: none; }

  .card--front .wordmark { position: absolute; left: 0; right: 0; top: 120px; justify-content: center; font-size: 56px; }
  .front-rule { position: absolute; height: 1px; background: var(--rule); }
  .front-rule--right { right: 0; width: 140px; top: 196px; }
  .front-rule--left { left: 0; width: 236px; top: 262px; }
  .front-url { position: absolute; left: 0; right: 0; top: 224px; text-align: center; font-size: 16px; color: var(--text-grey); }
  .front-url b, .contact b { color: var(--brand-blue); font-weight: 600; }

  .card--back .wordmark { position: absolute; left: 34px; top: 132px; font-size: 40px; }
  .card--back .wordmark__square { width: 26px; height: 26px; }
  .swoosh { position: absolute; inset: 0; }

  .contact { position: absolute; left: 306px; top: 26px; width: 240px; color: var(--text-grey); font-size: 12px; line-height: 18px; }
  .contact__name { color: var(--brand-blue); font-size: 16px; line-height: 22px; font-weight: 600; letter-spacing: .2px; }
  .contact__name small { color: var(--text-grey); font-size: 11px; font-weight: 400; }
  .contact__role { margin-bottom: 22px; }
  .contact__line { display: flex; align-items: center; gap: 7px; }
  .contact__icon { width: 13px; height: 13px; flex: none; }
</style>
</head>
<body>
<main class="stage">

  <section class="card card--front" aria-label="Card front">
    <div class="wordmark"><span class="wordmark__square"></span>velmotik</div>
    <span class="front-rule front-rule--right"></span>
    <p class="front-url">www.<b>velmotik</b>.com</p>
    <span class="front-rule front-rule--left"></span>
  </section>

  <section class="card card--back" aria-label="Card back">
    <svg class="swoosh" viewBox="0 0 560 320" aria-hidden="true">
      <path d="M0,292 C170,294 300,268 400,222 L560,204 L560,320 L0,320 Z" fill="var(--brand-grey)"/>
      <path d="M560,200 C470,212 396,256 358,320 L560,320 Z" fill="#ffffff"/>
      <path d="M560,210 C478,222 410,264 376,320 L560,320 Z" fill="var(--brand-blue)"/>
    </svg>

    <div class="wordmark"><span class="wordmark__square"></span>velmotik</div>

    <div class="contact">
      <p class="contact__name">MARC DELORME<small>, ing., M.Sc.A.</small></p>
      <p class="contact__role">Président | CEO</p>
      <p>412 – 88 Rue Lavallée Ouest,</p>
      <p>Laval (Québec) H7N 2K5 Canada</p>
      <p class="contact__line">
        <svg class="contact__icon" viewBox="0 0 14 14" aria-hidden="true"><rect width="14" height="14" rx="2" fill="var(--brand-blue)"/><path d="M4,3.5 L5.8,3.5 L6.3,5.6 L5.3,6.3 C5.8,7.4 6.6,8.2 7.7,8.7 L8.4,7.7 L10.5,8.2 L10.5,10 C7,10 4,7 4,3.5 Z" fill="#fff"/></svg>
        +1.450.218.0637
      </p>
      <p class="contact__line">
        <svg class="contact__icon" viewBox="0 0 14 14" aria-hidden="true"><rect width="14" height="14" rx="2" fill="var(--brand-blue)"/><rect x="3" y="4.2" width="8" height="5.6" fill="none" stroke="#fff" stroke-width="1"/><path d="M3,4.2 L7,7.3 L11,4.2" fill="none" stroke="#fff" stroke-width="1"/></svg>
        mdelorme@velmotik.com
      </p>
      <p class="contact__line">
        <svg class="contact__icon" viewBox="0 0 14 14" aria-hidden="true"><rect width="14" height="14" rx="2" fill="var(--brand-blue)"/><circle cx="7" cy="7" r="3.8" fill="none" stroke="#fff" stroke-width="1"/><ellipse cx="7" cy="7" rx="1.6" ry="3.8" fill="none" stroke="#fff" stroke-width=".8"/><path d="M3.2,7 H10.8" stroke="#fff" stroke-width=".8"/></svg>
        <span>www.<b>velmotik</b>.com</span>
      </p>
    </div>
  </section>

</main>
</body>
</html>
```